Pemberly & Associates Tax Services

Need an eye catching advertisement/lead generating design for prospects interesting in professional tax planning and tax preparation services. Ideas for
Sample Advertising Language is below:

We are accepting new clients!!
We are affordable and have over 20 years of experience serving the tax needs of our clientele.

Here are a few reasons you may want to contact us:

1. You want to learn how to maximize business deductions
2. You’re a high-income earner and want to learn ways to pay less in taxes
3. You have an interest in starting a business
4. You want to maximize rental property deductions
5. You have questions about maintaining a home office
6. You want to be updated periodically on tax law changes and tax planning strategies
7. You want to be represented by a tax expert before the FRB if you are subject to an audit

References available upon request.

Target Market(s)

Individuals, small businesses and startup business

Industry/Entity Type

Tax and Accounting Industry

Requirements
Nice to have
• Would like to develop a marketing campaign that can be used periodically to digitally generate leads, build email contact list of prospective clients who want to receive tax updates.

```html
<!DOCTYPE html>
<html lang="en">
<head>
<meta charset="utf-8">
<title>Pemberly &amp; Associates – Accepting New Clients</title>
<link href="https://fonts.googleapis.com/css2?family=Roboto+Slab:wght@400;500;700&family=Lobster&family=Roboto:wght@400;500&display=swap" rel="stylesheet">
<style>
:root{
  --stage:#8a8a8a;
  --blue:#1e5aa0;
  --blue-deep:#17468a;
  --blue-light:#3d7fcf;
  --green:#14a03a;
  --green-bright:#6bb52e;
  --green-text:#1a8f2e;
  --script-green:#5cc23f;
  --ink:#222;
  --ink-soft:#333;
  --white:#fff;
  --paper:#f6f7fa;
}
*{margin:0;padding:0;box-sizing:border-box}
html,body{width:1200px;height:1200px;overflow:hidden;background:var(--stage)}
.flyer{position:absolute;left:136px;top:0;width:928px;height:1200px;background:linear-gradient(180deg,var(--white) 0%,var(--paper) 60%,var(--white) 100%);overflow:hidden;font-family:'Roboto Slab',serif;color:var(--ink)}
.hero-photo{position:absolute;left:0;top:0;width:928px;height:300px;background:linear-gradient(180deg,#1b3766 0%,#2f5c9c 45%,var(--blue) 100%)}
.hero-waves{position:absolute;left:0;top:0}
.hero-kicker{position:absolute;left:44px;top:178px;font-weight:500;font-size:31px;color:var(--white);letter-spacing:.5px}
.hero-title{position:absolute;left:44px;top:214px;font-weight:700;font-size:51px;color:var(--white)}
.hero-tagline{position:absolute;left:44px;top:268px;width:600px;font-family:'Lobster',cursive;color:var(--white);line-height:32px}
.hero-tagline .small{font-size:17px}
.hero-tagline .accent{font-size:23px;color:var(--script-green)}
.hero-tagline .large{font-size:25px}
.team-photo{position:absolute;left:596px;top:17px;width:302px;height:302px;border-radius:50%;background:radial-gradient(circle at 45% 40%,#f2f2f2 0%,#d8dde3 55%,#9aa6b3 100%)}
.reasons-title{position:absolute;left:48px;top:412px;font-weight:700;font-size:23.5px;color:var(--ink)}
.reasons-title em{font-style:normal;color:var(--green-text)}
.reasons-rule{position:absolute;left:45px;top:452px;width:650px;height:2px;background:var(--green-text)}
.reasons{position:absolute;left:0;top:0;list-style:none}
.reasons li{position:absolute;left:101px;width:740px;font-size:21px;line-height:31px;color:var(--ink-soft)}
.reasons li svg{position:absolute;left:-57px;top:6px}
.references{position:absolute;left:60px;top:882px;width:309px;height:28px;background:var(--blue);border-radius:0 14px 14px 0;border:2px solid var(--blue-light);color:var(--white);font-weight:700;font-size:13.5px;line-height:24px;padding-left:8px}
.campaign{position:absolute;left:68px;top:918px;width:300px;font-size:14.8px;line-height:20.5px;color:var(--ink)}
.badge{position:absolute;left:68px;top:1056px;width:135px;height:34px;border:3px solid #b49a3a;border-right-color:#7aa7a0;border-bottom-color:#6d7f8e;background:var(--white)}
.brand{position:absolute;left:217px;top:1054px;display:flex;align-items:center;gap:6px}
.brand-dot{width:30px;height:30px;border-radius:50%;background:var(--blue)}
.brand-name{font-size:15px;line-height:17px;color:var(--blue);font-weight:500}
.meeting{position:absolute;left:388px;top:856px;width:540px;height:210px;background:linear-gradient(180deg,var(--blue) 0%,var(--blue-deep) 100%);border-radius:40px 40px 0 0}
.meeting-reflection{position:absolute;left:388px;top:1066px;width:540px;height:60px;background:linear-gradient(180deg,#d9dbe0 0%,rgba(255,255,255,0) 100%)}
.footer{position:absolute;left:0;top:1131px;width:928px;height:69px;background:linear-gradient(90deg,#168c2f,var(--green) 50%,#12942f);color:var(--white)}
.footer-firm{position:absolute;left:55px;top:17px;font-size:14.5px;line-height:18px}
.footer-firm small{font-size:12px;display:block}
.footer-divider{position:absolute;top:19px;width:2px;height:32px;background:var(--white)}
.footer-contact{position:absolute;left:255px;top:18px;font-size:12px;line-height:18px}
.footer-contact div{display:flex;align-items:center;gap:7px}
.footer-phone{position:absolute;left:600px;top:14px;display:flex;align-items:center;gap:20px;font-family:'Roboto',sans-serif;font-size:31px;font-weight:500}
</style>
</head>
<body>
<main class="flyer">
  <div class="hero-photo" role="img" aria-label="Business handshake photograph over a night city skyline"></div>
  <svg class="hero-waves" width="928" height="440" viewBox="0 0 928 440">
    <path d="M0 0H928V428C820 392 690 372 560 380C380 392 200 400 0 372Z" fill="#0f9236"/>
    <path d="M0 0H928V400C760 330 600 330 430 352C260 372 120 372 0 356Z" fill="#6bb52e"/>
    <path d="M0 0H928V300C760 300 620 330 470 346C300 360 150 350 0 346Z" fill="#2d8f8a"/>
    <path d="M0 300H928V0H0Z" fill="none"/>
    <path d="M0 260C150 270 300 280 420 300C560 320 720 300 928 250V0H928V250C720 320 520 340 0 342Z" fill="#1e5aa0"/>
    <path d="M0 230H928V250C720 320 520 340 0 342Z" fill="#1e5aa0"/>
    <circle cx="747" cy="166" r="178" fill="#ffffff"/>
    <circle cx="747" cy="166" r="175" fill="#1e5aa0"/>
  </svg>
  <div class="team-photo" role="img" aria-label="Photograph of a presenter beside a chart board with colleagues seated at a meeting table"></div>
  <p class="hero-kicker">WE ARE ACCEPTING</p>
  <h1 class="hero-title">NEW CLIENTS!!</h1>
  <p class="hero-tagline"><span class="small">We are affordable and have over </span><span class="accent">20 years of experience</span> <span class="large">Serving the<br>tax needs of our clientele.</span></p>

  <h2 class="reasons-title">Here are a <em>few reasons</em> you may want to contact us:</h2>
  <div class="reasons-rule"></div>
  <ul class="reasons">
    <li style="top:551px"><svg width="36" height="30" viewBox="0 0 36 30"><path d="M2 15L12 28L34 2L12 20Z" fill="#1e5aa0"/></svg>You want to learn how to maximize business deductions</li>
    <li style="top:597px"><svg width="36" height="30" viewBox="0 0 36 30"><path d="M2 15L12 28L34 2L12 20Z" fill="#1e5aa0"/></svg>You have an interest in starting a business</li>
    <li style="top:648px"><svg width="36" height="30" viewBox="0 0 36 30"><path d="M2 15L12 28L34 2L12 20Z" fill="#1e5aa0"/></svg>You have questions about maintaining a home office</li>
    <li style="top:698px"><svg width="36" height="30" viewBox="0 0 36 30"><path d="M2 15L12 28L34 2L12 20Z" fill="#1e5aa0"/></svg>You want to maximize rental property deductions</li>
    <li style="top:748px"><svg width="36" height="30" viewBox="0 0 36 30"><path d="M2 15L12 28L34 2L12 20Z" fill="#1e5aa0"/></svg>You’re a high-income earner and want to learn ways to pay less in taxes</li>
    <li style="top:798px;width:700px"><svg width="36" height="30" viewBox="0 0 36 30"><path d="M2 15L12 28L34 2L12 20Z" fill="#1e5aa0"/></svg>You want to be represented by a tax expert before the FRB if you are subject to an audit</li>
    <li style="top:879px;width:700px"><svg width="36" height="30" viewBox="0 0 36 30"><path d="M2 15L12 28L34 2L12 20Z" fill="#1e5aa0"/></svg>You want to be updated periodically on tax law changes and tax planning strategies</li>
  </ul>

  <div class="references" style="top:962px">REFERENCES AVAILABLE UPON REQUEST</div>
  <p class="campaign" style="top:1002px">Would like to develop a marketing campaign that can be used periodically to digitally generate leads, build email contact list of prospective clients who want to receive tax update newsletters</p>
  <div class="badge" style="top:1134px"></div>
  <div class="brand" style="top:1132px">
    <span class="brand-dot"></span>
    <span class="brand-name">Pemberly &amp;<br>Associates LLC</span>
  </div>

  <div class="meeting" style="top:935px;height:200px" role="img" aria-label="Silhouettes of business people seated around a conference table"></div>

  <footer class="footer">
    <div class="footer-firm">Pemberly &amp; Associates<small>Tax and Business Services</small></div>
    <span class="footer-divider" style="left:237px"></span>
    <div class="footer-contact">
      <div><svg width="9" height="12" viewBox="0 0 9 12"><path d="M4.5 0A4.5 4.5 0 0 0 0 4.5C0 8 4.5 12 4.5 12S9 8 9 4.5A4.5 4.5 0 0 0 4.5 0ZM4.5 6.3A1.8 1.8 0 1 1 4.5 2.7 1.8 1.8 0 0 1 4.5 6.3Z" fill="#fff"/></svg>4870 Harbor View Rd., Suite 210-140 Fairmont, CA 95890</div>
      <div><svg width="11" height="8" viewBox="0 0 11 8"><rect width="11" height="8" fill="#fff"/><path d="M0 0L5.5 4.5L11 0" stroke="#14a03a" fill="none"/></svg>ledgerdesk@example.com</div>
    </div>
    <span class="footer-divider" style="left:584px"></span>
    <div class="footer-phone">
      <svg width="26" height="26" viewBox="0 0 24 24"><path d="M6.6 10.8a15 15 0 0 0 6.6 6.6l2.2-2.2a1 1 0 0 1 1-.25 11.4 11.4 0 0 0 3.6.57 1 1 0 0 1 1 1V20a1 1 0 0 1-1 1A17 17 0 0 1 3 4a1 1 0 0 1 1-1h3.5a1 1 0 0 1 1 1c0 1.25.2 2.45.57 3.57a1 1 0 0 1-.25 1Z" fill="none" stroke="#fff" stroke-width="1.6"/></svg>
      <span>(555) 204-7816</span>
    </div>
  </footer>
</main>
</body>
</html>
```